Brevan Power Services Website - Solar Sales and Installation and Renewable Energy Marketing

I need a website for my solar sales and installation/renewable energy marketing company. We will focus on solar, so the web page should make that a main focus. Ideally it will have 5-6 total pages. One main page, one page "Why Solar", "Our Services", "About Us", "Contact Us", and some type of page that collects leads or information from customers who are interested in a solar quote. Our image focus should be either residential solar panels or windmills (renewable energy). The logo, attached, is green and orange. The color scheme should be predominantly white, clean cut, with orange/green buttons or accents. I don't want to have a blog-like page, it should mimic other solar company websites. A good example would be Caldrex's solar website.

```html
<!DOCTYPE html>
<html lang="en">
<head>
<meta charset="utf-8">
<title>Brevan Power Services</title>
<link href="https://fonts.googleapis.com/css2?family=Mulish:wght@400;600;700;800&display=swap" rel="stylesheet">
<style>
:root{
  --orange:#ff7300;
  --green:#9cff00;
  --ink:#1f1f1f;
  --text:#333;
  --nav:#efefef;
  --white:#fff;
  --footer:#1b1d21;
  --muted:#b9bcc2;
  --neutral:#9a9a9a;
}
*{box-sizing:border-box;margin:0;padding:0}
html,body{width:1200px;height:4060px;overflow:hidden;background:var(--white)}
body{position:relative;font-family:"Mulish",sans-serif;color:var(--text)}
.abs{position:absolute}
.btn{position:absolute;height:55px;border-radius:28px;display:flex;align-items:center;justify-content:center;gap:10px;font-weight:800;font-size:18px;color:var(--white);background:var(--orange)}
.btn.green{background:var(--green);color:var(--ink)}
.btn .arrow{width:17px;height:17px;border-radius:50%;background:currentColor;position:relative}
.btn .arrow::after{content:"";position:absolute;left:5px;top:4.5px;border:4px solid transparent;border-left:6px solid var(--orange)}
.btn.green .arrow::after{border-left-color:var(--green)}
.accent{color:var(--orange)}
h2.section-title{position:absolute;font-weight:400;font-size:46px;color:var(--ink);white-space:nowrap}
h2.section-title .accent{font-weight:700}

/* header */
.topbar{top:0;left:0;width:1200px;height:113px}
.call{left:200px;top:34px;display:flex;gap:10px;align-items:center}
.call .label,.search .label{font-size:17px;color:var(--ink);line-height:1.3}
.call .num{font-size:17px;font-weight:800;color:var(--orange)}
.brand{left:490px;top:4px;display:flex;align-items:center;gap:14px}
.brand .mark{width:64px;height:64px;border-radius:50%;border:3px solid var(--neutral)}
.brand .rule{width:2px;height:104px;background:#555}
.brand .name{font-size:20px;font-weight:700;letter-spacing:2px;line-height:1.15;color:#2a2a2a}
.search{left:805px;top:34px;display:flex;gap:12px;align-items:center}
.search .hint{font-size:17px;color:#444}
.navbar{top:113px;left:0;width:1200px;height:62px;background:var(--nav)}
.navbar a{position:absolute;top:19px;transform:translateX(-50%);font-size:20px;letter-spacing:3px;color:#333;text-decoration:none;white-space:nowrap}
.navbar a.active{font-weight:800;color:var(--ink)}
.navbar a.active::after{content:"";position:absolute;left:50%;bottom:-8px;width:30px;height:3px;margin-left:-15px;background:var(--orange);border-radius:2px}

/* hero */
.hero{top:175px;left:0;width:1200px;height:716px;overflow:hidden}
.hero-photo{position:absolute;inset:0;background:linear-gradient(180deg,#8cb7e6 0%,#a9c8ea 30%,#5d7fb9 52%,#34538e 70%,#59684a 88%,#6d7a4f 100%)}
.hero-curve{position:absolute;left:0;top:0}
.hero-brand{position:absolute;top:118px;width:1200px;text-align:center;font-size:40px;font-weight:700;letter-spacing:4px;color:var(--ink)}
.hero h1{position:absolute;top:210px;width:1200px;text-align:center;font-size:57px;font-weight:700;color:var(--ink)}
.hero p{position:absolute;top:294px;width:1200px;text-align:center;font-size:22px;font-weight:600;color:#222;line-height:44px}
.hero .btn{left:505px;top:401px;width:205px}

/* welcome */
.welcome-title{top:960px;left:0;width:1200px;text-align:center}
.welcome-text{top:1028px;left:142px;width:916px;text-align:center;font-size:18px;line-height:36px;color:#333}
.divider{top:1290px;left:90px;width:1020px;height:1px;background:#e4e4e4}

/* about */
.about-photo{left:120px;top:1372px;width:355px;height:442px;border-radius:50%;background:radial-gradient(ellipse at 40% 45%,#cfd9e8 0%,#7d8cb8 45%,#3f4c86 100%)}
.about-text{left:563px;top:1494px;width:535px;font-size:16px;line-height:36px;text-align:justify;color:#333}

/* services */
.provide{top:1895px;left:0;width:1200px;height:935px}
.service{position:absolute;width:340px;text-align:center;transform:translateX(-50%)}
.service .ring{position:relative;width:260px;height:260px;margin:0 auto}
.service .photo{position:absolute;left:34px;top:34px;width:220px;height:220px;border-radius:50%}
.service h3{margin-top:18px;font-size:32px;font-weight:600;color:#2a2a2a;line-height:36px}
.dots{position:absolute;top:2576px;left:561px;display:flex;gap:8px}
.dots span{width:17px;height:17px;border-radius:50%;border:2px solid #333}
.dots span.on{background:#333}

/* why solar */
.why-text{left:90px;top:2996px;width:583px;font-size:18px;line-height:40px;text-align:justify;color:#333}
.why-list{left:90px;top:3122px;list-style:none;font-size:17px;font-weight:800;color:#2a2a2a}
.why-list li{height:45px;display:flex;align-items:center;gap:8px}
.why-list li::before{content:"";width:7px;height:14px;background:var(--orange);clip-path:polygon(60% 0,0 60%,45% 60%,30% 100%,100% 40%,55% 40%)}
.why-photo{left:716px;top:2922px;width:420px;height:420px;border-radius:50%;background:radial-gradient(circle at 80% 55%,#f2c489 0%,#a07e6e 25%,#3d4968 55%,#1a2238 100%)}

/* footer */
.footer{top:3420px;left:0;width:1200px;height:640px}
.footer-brand{left:87px;top:3628px;display:flex;align-items:center;gap:16px}
.footer-brand .mark{width:84px;height:84px;border-radius:50%;border:3px solid var(--muted)}
.footer-brand .rule{width:2px;height:124px;background:#777}
.footer-brand .name{font-size:23px;font-weight:800;letter-spacing:2px;line-height:1.2;color:var(--white)}
.follow{left:831px;top:3725px;display:flex;align-items:center;gap:6px;color:var(--white);font-size:15px;font-weight:800}
.follow .social{width:29px;height:29px;border-radius:50%;border:1.5px solid var(--white)}
.footer-rule{top:3778px;left:90px;width:1020px;height:1px;background:#4a4c52}
.fcol{top:3810px}
.fcol h4{font-size:15px;font-weight:800;color:var(--white);margin-bottom:22px}
.fcol li{list-style:none;font-size:14px;line-height:27px;color:var(--muted)}
.contact-row{display:flex;gap:10px;font-size:12.5px;line-height:24px;color:var(--muted);margin-bottom:14px}
.contact-row svg{flex:none;margin-top:5px}
.newsletter-input{left:836px;top:3853px;width:274px;height:38px;background:var(--white);border-radius:3px;font-size:11px;color:#999;padding:12px 14px}
.subscribe{left:836px;top:3910px;width:154px;height:40px;border-radius:20px;background:var(--orange);color:var(--white);font-size:17px;font-weight:600;display:flex;align-items:center;justify-content:center}
.copyright{top:4015px;left:0;width:1200px;text-align:center;font-size:13px;color:var(--muted)}
</style>
</head>
<body>

<header class="abs topbar">
  <div class="abs call">
    <svg width="42" height="42" viewBox="0 0 42 42"><circle cx="21" cy="21" r="18" fill="none" stroke="#ff7300" stroke-width="2.5"/><path d="M14 12c2-1 3 0 4 3s-1 3-1 4 3 5 5 6 2-2 4-1 3 2 2 4-3 3-6 1-9-8-9-12 0-4 1-5z" fill="#ff7300"/></svg>
    <div><div class="label">Call us:</div><div class="num">1-800-555-0142</div></div>
  </div>
  <div class="abs brand">
    <div class="mark"></div>
    <div class="rule"></div>
    <div class="name">BREVAN<br>POWER<br>SERVICES</div>
  </div>
  <div class="abs search">
    <svg width="42" height="42" viewBox="0 0 42 42"><circle cx="17" cy="17" r="12" fill="none" stroke="#ff7300" stroke-width="3"/><path d="M26 26l11 11" stroke="#ff7300" stroke-width="5" stroke-linecap="round"/></svg>
    <div><div class="label">Search:</div><div class="hint">Enter search here...</div></div>
  </div>
</header>

<nav class="abs navbar">
  <a class="active" style="left:131px">HOME</a>
  <a style="left:323px">WHY SOLAR</a>
  <a style="left:568px">OUR SERVICES</a>
  <a style="left:801px">ABOUT US</a>
  <a style="left:1023px">CONTACT US</a>
</nav>

<section class="abs hero">
  <div class="hero-photo" role="img" aria-label="Rows of solar panels in a field with wind turbines under a blue sky"></div>
  <div class="hero-brand">BREVAN</div>
  <h1>Solar Energy Services</h1>
  <p>Lorem ipsum dolor sit amet, consectetur adipiscing elit, sed do eiusmod<br>tempor incididunt ut labore et dolore magna aliqua.</p>
  <div class="btn">Read More <span class="arrow"></span></div>
  <svg class="hero-curve" width="1200" height="716" viewBox="0 0 1200 716">
    <path d="M0,511 C320,615 620,697 840,697 C1000,697 1120,645 1200,585 L1200,716 L0,716 Z" fill="#ff7300"/>
    <path d="M0,519 C320,625 600,705 780,716 L0,716 Z" fill="#fff"/>
    <path d="M780,716 C900,716 1000,716 1200,716 L1200,625 C1120,690 990,716 840,716 Z" fill="#fff"/>
  </svg>
</section>

<h2 class="section-title welcome-title">Welcome to <span class="accent" style="font-weight:600">Brevan Power Solutions</span></h2>
<p class="abs welcome-text">Our mission is to give cost-effective and effective power alternatives and items which are self-sustainable. One of the key inclusions of our mission viewpoint is the participation of the group in creating power alternatives for self and becoming a role model for others.</p>
<div class="btn" style="left:388px;top:1156px;width:205px">Read More <span class="arrow"></span></div>
<div class="btn green" style="left:607px;top:1156px;width:205px">Our Products <span class="arrow"></span></div>
<div class="abs divider"></div>

<div class="abs about-photo" role="img" aria-label="Solar installations and buildings framed in an oval"></div>
<h2 class="section-title" style="left:563px;top:1425px">About <span class="accent">BPS</span></h2>
<p class="abs about-text">Brevan Power Solutions is a leading organization based in Rivermoor, affianced in the area of Distributing, Trading and Service Providing for Grid-tied &amp; Off-grid solar power plants, Solar water pumping, Solar water heaters, solar street lights &amp; other types of equipment related to Green Energy.</p>
<div class="btn" style="left:563px;top:1687px;width:205px">Read More <span class="arrow"></span></div>

<section class="abs provide">
  <svg class="abs" style="left:0;top:0" width="1200" height="935" viewBox="0 0 1200 935">
    <defs>
      <linearGradient id="mist" x1="0" y1="0" x2="0" y2="1">
        <stop offset="0" stop-color="#e9e6e6"/>
        <stop offset="0.45" stop-color="#f1e4df"/>
        <stop offset="0.75" stop-color="#e8e0dc"/>
        <stop offset="1" stop-color="#f3f1ef"/>
      </linearGradient>
    </defs>
    <path d="M0,130 C120,40 300,5 500,15 C780,30 1000,120 1200,205 L1200,935 L0,935 Z" fill="#9cff00"/>
    <path d="M0,145 C130,60 310,25 510,35 C790,52 1010,150 1200,215 L1200,935 L0,935 Z" fill="url(#mist)" role="img" aria-label="Wind turbines reflected in a calm lake at dusk"/>
    <path d="M0,722 C250,820 520,910 760,905 C960,900 1110,860 1200,815 L1200,935 L0,935 Z" fill="#ff7300"/>
    <path d="M0,730 C240,845 500,925 700,935 L0,935 Z" fill="#fff"/>
    <path d="M700,935 C900,935 1080,900 1200,850 L1200,935 Z" fill="#fff"/>
  </svg>
  <h2 class="section-title" style="left:0;width:1200px;text-align:center;top:222px">We <span class="accent">Provide</span></h2>
</section>

<div class="service" style="left:232px;top:2200px">
  <div class="ring">
    <svg class="abs" style="left:0;top:0" width="290" height="260" viewBox="0 0 290 260"><path d="M6,150 A140,140 0 0 1 230,32" fill="none" stroke="#9cff00" stroke-width="14"/><path d="M284,150 A140,140 0 0 1 140,265" fill="none" stroke="#ff7300" stroke-width="14"/></svg>
    <div class="photo" style="background:radial-gradient(circle at 40% 40%,#4a5572,#161b29)" role="img" aria-label="Close view of dark solar panel surfaces"></div>
  </div>
  <h3>Solar Sales</h3>
</div>
<div class="service" style="left:601px;top:2200px">
  <div class="ring">
    <svg class="abs" style="left:0;top:0" width="290" height="260" viewBox="0 0 290 260"><path d="M6,150 A140,140 0 0 1 230,32" fill="none" stroke="#9cff00" stroke-width="14"/><path d="M284,150 A140,140 0 0 1 140,265" fill="none" stroke="#ff7300" stroke-width="14"/></svg>
    <div class="photo" style="background:linear-gradient(180deg,#7fa6dc 0%,#b9cde6 40%,#3b5ea6 62%,#263f7a 100%)" role="img" aria-label="Installer fitting solar panels on a roof"></div>
  </div>
  <h3>Solar Installation</h3>
</div>
<div class="service" style="left:963px;top:2200px">
  <div class="ring">
    <svg class="abs" style="left:0;top:0" width="290" height="260" viewBox="0 0 290 260"><path d="M6,150 A140,140 0 0 1 230,32" fill="none" stroke="#9cff00" stroke-width="14"/><path d="M284,150 A140,140 0 0 1 140,265" fill="none" stroke="#ff7300" stroke-width="14"/></svg>
    <div class="photo" style="background:linear-gradient(180deg,#dfe6ee 0%,#c9d2dd 35%,#3a4a6b 60%,#6f8a4d 100%)" role="img" aria-label="Solar array next to a small house"></div>
  </div>
  <h3>Renewable Energy Marketing</h3>
</div>
<div class="dots"><span></span><span class="on"></span><span></span></div>

<h2 class="section-title" style="left:90px;top:2935px">Why <span class="accent">Solar</span></h2>
<p class="abs why-text">Lorem ipsum dolor sit amet, consectetur adipiscing elit, sed do eiusmod tempor incididunt ut labore et dolore magna aliqua. Quis ipsum suspendisse ultrices gravida.</p>
<ul class="abs why-list">
  <li>Generate Your Own Power</li>
  <li>Reap the Returns</li>
  <li>Heal the World</li>
</ul>
<div class="btn" style="left:90px;top:3261px;width:205px">Read More <span class="arrow"></span></div>
<svg class="abs" style="left:690px;top:2900px" width="470" height="460" viewBox="0 0 470 460"><circle cx="232" cy="228" r="222" fill="none" stroke="#ff7300" stroke-width="5"/><path d="M30,160 A215,215 0 0 1 400,95" fill="none" stroke="#ff7300" stroke-width="9"/></svg>
<div class="abs why-photo" role="img" aria-label="Solar panels at sunset"></div>

<footer class="abs footer">
  <svg class="abs" style="left:0;top:0" width="1200" height="640" viewBox="0 0 1200 640">
    <defs>
      <linearGradient id="night" x1="0" y1="0" x2="0" y2="1">
        <stop offset="0" stop-color="#2a2d33"/>
        <stop offset="1" stop-color="#15171a"/>
      </linearGradient>
    </defs>
    <path d="M0,130 C130,50 300,10 480,20 C760,35 1000,130 1200,225 L1200,640 L0,640 Z" fill="#9cff00"/>
    <path d="M0,148 C140,72 310,38 490,46 C770,60 1010,160 1200,235 L1200,640 L0,640 Z" fill="url(#night)" role="img" aria-label="Dark field of solar panels with power pylons"/>
  </svg>
</footer>
<div class="abs footer-brand">
  <div class="mark"></div>
  <div class="rule"></div>
  <div class="name">BREVAN<br>POWER<br>SERVICES</div>
</div>
<div class="abs follow">FOLLOW US :
  <span class="social" aria-label="Social profile"></span>
  <span class="social" aria-label="Social profile"></span>
  <span class="social" aria-label="Social profile"></span>
  <span class="social" aria-label="Social profile"></span>
  <span class="social" aria-label="Social profile"></span>
</div>
<div class="abs footer-rule"></div>

<div class="abs fcol" style="left:91px">
  <h4>NAVIGATION</h4>
  <ul><li>Home</li><li>Our Services</li><li>Why Solar</li><li>About Us</li><li>Contact Us</li></ul>
</div>
<div class="abs fcol" style="left:298px">
  <h4>LINKS</h4>
  <ul><li>Terms &amp; Conditions</li><li>Privacy Policy</li><li>Site Map</li><li>Disclaimer</li></ul>
</div>
<div class="abs fcol" style="left:522px;width:280px">
  <h4>CONTACT INFO</h4>
  <div class="contact-row"><svg width="12" height="15" viewBox="0 0 12 15"><path d="M6 1a5 5 0 0 1 5 5c0 4-5 8-5 8S1 10 1 6a5 5 0 0 1 5-5z" fill="none" stroke="#b9bcc2" stroke-width="1.5"/><circle cx="6" cy="6" r="1.8" fill="#b9bcc2"/></svg><span>#52, Larkspur Trade Park, Sector 9,<br>Rivermoor- 402117</span></div>
  <div class="contact-row"><svg width="12" height="12" viewBox="0 0 12 12"><path d="M2 1c1-.5 2 0 2.5 1.5S4 4 4 4.5s1.8 3 3 3.5 1-1 2-.5 2 1 1.5 2-2 1.5-3.5.5S1 6 1 3.5 1.5 1.5 2 1z" fill="#b9bcc2"/></svg><span style="font-size:14px">Help :+91-9400017265</span></div>
  <div class="contact-row"><svg width="13" height="10" viewBox="0 0 13 10"><rect x="0.5" y="0.5" width="12" height="9" fill="none" stroke="#b9bcc2"/><path d="M0.5 0.5l6 5 6-5" fill="none" stroke="#b9bcc2"/></svg><span style="font-size:14px">info@brevanpowersolutions.com</span></div>
</div>
<div class="abs fcol" style="left:836px">
  <h4>NEWSLETTER</h4>
</div>
<div class="abs newsletter-input">Enter e-mail address</div>
<div class="abs subscribe">Subscribe</div>
<p class="abs copyright">Copyrights© Brevan. 2019 | Allrights Reserved.</p>

</body>
</html>
```